Mirelo Japanese Restaurant

We just want the japanese sakura background and the menu as below

Side dish :
Edamame $4
Japanese Steam Green Bean
Crab Craw $3 each
With Japanese mayo
Teriyaki Chicken stick $3 each
Chicken stick with home made teriyaki sauce
Tempura Prawns $7
With Japanese mayo
Miso Soup $3
Traditional Japanese soup
Salt and Pepper Calamari $7
With japanese mayo

Main dish:
Gyu Don $12
Bowl of steam rice topped with beef and onion simmered in a mildly sweet sauce.
Teriyaki Don $12
Bowl of steam rice topped with your choice of beef, chicken or pork and with our special Teriyaki sauce.
Vege Don $12
Bowl of steam rice with seasonal Vegetables with the special japanese sweet soy sauce.
Japanese Curry $12,(prawns $14)
Bowl of steam rice with Chicken, pork or prawn with japanese mild curry sauce.
Katsu Don $12
Bowl of steam rice topped with a deep-fried pork cutlet and egg with the japanese special sauce.
Oyako Don $12
Bowl of steam rice topped with chick and egg with japanese special sauce.
Spice Don $12
Bowl of steam rice topped with beef or chicken with japanese spice sauce.
Gingle Don $12
Bowl of steam rice topped with beef or chicken with japanese ginger sauce.
Sushi $3
Roll everyday on seasonal
ingredient.

Japanese-style sweets
Black Sesame Ice cream $4.5
Green tea Ice cream $4.5

```html
<!DOCTYPE html>
<html lang="en">
<head>
<meta charset="utf-8">
<title>Mirelo Japanese Restaurant – Menu</title>
<link href="https://fonts.googleapis.com/css2?family=Jost:ital,wght@0,400;0,500;0,600;1,400&family=Pirata+One&display=swap" rel="stylesheet">
<style>
  :root {
    --canvas: #ecebe8;
    --paper: #fbf4f2;
    --blossom: #f3dfe2;
    --frame: #1c1c1c;
    --band: #e9dcc0;
    --band-dark: #dccaa2;
    --ink: #141414;
    --ink-soft: #444;
    --leader: #9a9a9a;
    --accent: #d3123d;
    --pink: #ee6fa8;
  }
  * { box-sizing: border-box; margin: 0; padding: 0; }
  html, body { width: 1200px; height: 889px; overflow: hidden; }
  body {
    background: var(--canvas);
    font-family: "Jost", "Futura", sans-serif;
    color: var(--ink);
    position: relative;
  }
  .menu-page {
    position: absolute;
    top: 73px;
    width: 545px;
    height: 778px;
    background: var(--paper);
  }
  .menu-page--main { left: 26px; }
  .menu-page--side { left: 626px; }
  .page-frame {
    position: absolute;
    left: 14px; top: 19px;
    width: 517px; height: 742px;
    border: 2px solid var(--frame);
    overflow: hidden;
    background:
      radial-gradient(ellipse 260px 180px at 30% 18%, var(--blossom), transparent 70%),
      radial-gradient(ellipse 300px 220px at 60% 70%, #efe5e8, transparent 70%),
      var(--paper);
  }
  .sakura-backdrop {
    position: absolute; inset: 94px 0 28px 0;
    background: linear-gradient(180deg, rgba(243,223,226,.55), rgba(235,232,236,.35) 60%, rgba(243,223,226,.4));
  }
  .page-header {
    position: absolute; left: 0; top: 0; width: 100%; height: 94px;
    background: linear-gradient(180deg, var(--band), var(--band-dark));
    border-bottom: 2px solid var(--frame);
  }
  .brand-dot {
    position: absolute; left: 14px; top: 19px;
    width: 54px; height: 54px; border-radius: 50%;
    background: var(--accent);
  }
  .brand-name {
    position: absolute; left: 95px; top: 8px; width: 320px;
    text-align: center; font-weight: 500; line-height: 1.2;
  }
  .brand-name .brand-line-1 { display: block; font-size: 32px; }
  .brand-name .brand-line-2 { display: block; font-size: 28px; }
  .header-art {
    position: absolute; right: 0; top: 0; width: 96px; height: 92px;
    border-left: 2px solid var(--frame);
    background: linear-gradient(160deg, #f6eef0, #e9d6da 55%, #d9dde3);
  }
  .section-title {
    position: absolute; left: 20px;
    font-family: "Pirata One", "Georgia", serif;
    color: var(--accent); font-size: 44px; font-weight: 400; line-height: 1;
    letter-spacing: 1px;
  }
  .section-title--sweets { font-size: 36px; line-height: 1.02; }
  .menu-item { position: absolute; left: 21px; width: 249px; }
  .item-row { display: flex; align-items: baseline; }
  .item-name { font-size: 18px; font-weight: 500; white-space: nowrap; }
  .item-leader { flex: 1; border-bottom: 1px solid var(--leader); margin: 0 4px; transform: translateY(-4px); }
  .item-each { font-size: 13px; font-style: italic; font-weight: 500; margin-right: 5px; }
  .item-price { font-size: 18px; font-weight: 500; white-space: nowrap; }
  .item-variant { font-size: 11px; font-style: italic; font-weight: 600; margin-top: -2px; }
  .item-desc { font-size: 10.5px; font-style: italic; color: var(--ink-soft); line-height: 1.3; }
  .food-photo {
    position: absolute; left: 295px; width: 196px; border-radius: 8px;
  }
  .food-photo--bowl { background: radial-gradient(circle at 50% 50%, #b8692f, #8c3a1e 45%, #c2151e 62%, #3a2a25); }
  .food-photo--curry { background: radial-gradient(circle at 50% 50%, #d9a543, #b87a2c 45%, #c2151e 64%, #3a2a25); }
  .food-photo--fried { background: radial-gradient(circle at 45% 45%, #d98a3c, #b45f22 40%, #8fbf55 70%, #e9eef0); }
  .food-photo--dessert { background: radial-gradient(circle at 40% 45%, #9aa46a, #4a4a2a 45%, #2a2420); }
  .divider { position: absolute; left: 20px; width: 470px; height: 2px; background: var(--accent); }
  .blossom-art {
    position: absolute; left: 402px; top: 643px; width: 72px; height: 74px;
    border-radius: 50%;
    background: radial-gradient(circle, #f7b9d5, var(--pink) 70%, transparent 72%);
  }
  .page-footer {
    position: absolute; left: 0; bottom: 0; width: 100%; height: 28px;
    background: var(--band); border-top: 2px solid var(--frame);
    display: flex; align-items: center; justify-content: center;
    font-size: 12.5px; font-weight: 600; letter-spacing: .3px;
  }
  .page-footer .sep { color: var(--accent); margin: 0 6px; }
</style>
</head>
<body>

<section class="menu-page menu-page--main">
  <div class="page-frame">
    <div class="sakura-backdrop" role="img" aria-label="Soft sakura blossom branches and mountain background"></div>
    <header class="page-header">
      <span class="brand-dot"></span>
      <h1 class="brand-name"><span class="brand-line-1">Mirelo</span><span class="brand-line-2">Japanese Restaurant</span></h1>
      <div class="header-art" role="img" aria-label="Cherry blossom branch illustration"></div>
    </header>

    <h2 class="section-title" style="top:112px">Main Dish</h2>

    <div class="menu-item" style="top:166px"><div class="item-row"><span class="item-name">Gyu Don</span><span class="item-leader"></span><span class="item-price">$12</span></div><p class="item-desc">Bowl of steam rice topped with beef and onion simmered in a mildly sweet sauce.</p></div>
    <div class="menu-item" style="top:226px"><div class="item-row"><span class="item-name">Teriyaki Don</span><span class="item-leader"></span><span class="item-price">$12</span></div><p class="item-desc">Bowl of steam rice topped with your choice of beef, chicken or pork and with our special Teriyaki sauce.</p></div>
    <div class="menu-item" style="top:286px"><div class="item-row"><span class="item-name">Vege Don</span><span class="item-leader"></span><span class="item-price">$12</span></div><p class="item-desc">Bowl of steam rice with seasonal Vegetables with the special japanese sweet soy sauce.</p></div>
    <div class="menu-item" style="top:346px"><div class="item-row"><span class="item-name">Japanese Curry</span><span class="item-leader"></span><span class="item-price">$12</span></div><p class="item-variant">(Prawns _ $14)</p><p class="item-desc">Bowl of steam rice with Chicken, pork or prawn with japanese mild curry sauce.</p></div>
    <div class="menu-item" style="top:423px"><div class="item-row"><span class="item-name">Katsu Don</span><span class="item-leader"></span><span class="item-price">$12</span></div><p class="item-desc">Bowl of steam rice topped with a deep-fried pork cutlet and egg with the japanese special sauce.</p></div>
    <div class="menu-item" style="top:483px"><div class="item-row"><span class="item-name">Oyako Don</span><span class="item-leader"></span><span class="item-price">$12</span></div><p class="item-desc">Bowl of steam rice topped with chick and egg with japanese special sauce.</p></div>
    <div class="menu-item" style="top:543px"><div class="item-row"><span class="item-name">Spice Don</span><span class="item-leader"></span><span class="item-price">$12</span></div><p class="item-desc">Bowl of steam rice topped with beef or chicken with japanese spice sauce.</p></div>
    <div class="menu-item" style="top:603px"><div class="item-row"><span class="item-name">Gingle Don</span><span class="item-leader"></span><span class="item-price">$12</span></div><p class="item-desc">Bowl of steam rice topped with beef or chicken with japanese ginger sauce.</p></div>
    <div class="menu-item" style="top:663px"><div class="item-row"><span class="item-name">Sushi</span><span class="item-leader"></span><span class="item-price">$3</span></div><p class="item-desc">Roll everyday on seasonal ingredient.</p></div>

    <div class="food-photo food-photo--bowl" style="top:114px;height:136px" role="img" aria-label="Photo of a rice bowl topped with beef and vegetables"></div>
    <div class="food-photo food-photo--bowl" style="top:261px;height:137px" role="img" aria-label="Photo of a teriyaki rice bowl with sesame"></div>
    <div class="food-photo food-photo--curry" style="top:408px;height:137px" role="img" aria-label="Photo of Japanese curry with chicken and potato"></div>
    <div class="food-photo food-photo--curry" style="top:558px;height:137px" role="img" aria-label="Photo of Japanese curry with a fried prawn"></div>

    <footer class="page-footer">T14 CORAL BAY SHOPPING CENTRE<span class="sep">•</span>OPEN 7 DAYS A WEEK 10AM – 9PM</footer>
  </div>
</section>

<section class="menu-page menu-page--side">
  <div class="page-frame">
    <div class="sakura-backdrop" role="img" aria-label="Soft sakura blossom branches and mountain background"></div>
    <header class="page-header">
      <span class="brand-dot"></span>
      <h1 class="brand-name"><span class="brand-line-1">Mirelo</span><span class="brand-line-2">Japanese Restaurant</span></h1>
      <div class="header-art" role="img" aria-label="Cherry blossom branch illustration"></div>
    </header>

    <h2 class="section-title" style="top:112px">Side Dish</h2>

    <div class="menu-item" style="top:166px"><div class="item-row"><span class="item-name">Edamame</span><span class="item-leader"></span><span class="item-price">$4</span></div><p class="item-desc">Japanese Steam Green Bean</p></div>
    <div class="menu-item" style="top:216px"><div class="item-row"><span class="item-name">Crab Craw</span><span class="item-leader"></span><span class="item-each">each</span><span class="item-price">$3</span></div><p class="item-desc">With Japanese mayo</p></div>
    <div class="menu-item" style="top:266px"><div class="item-row"><span class="item-name">Teriyaki Chicken stick</span><span class="item-leader"></span><span class="item-each">each</span><span class="item-price">$3</span></div><p class="item-desc">Chicken stick with home made teriyaki sauce</p></div>
    <div class="menu-item" style="top:316px"><div class="item-row"><span class="item-name">Tempura Prawns</span><span class="item-leader"></span><span class="item-price">$7</span></div><p class="item-desc">With Japanese mayo</p></div>
    <div class="menu-item" style="top:366px"><div class="item-row"><span class="item-name">Miso Soup</span><span class="item-leader"></span><span class="item-price">$3</span></div><p class="item-desc">Traditional Japanese soup</p></div>
    <div class="menu-item" style="top:412px"><div class="item-row"><span class="item-name">Salt &amp; Pepper Calamari</span><span class="item-leader"></span><span class="item-price">$7</span></div><p class="item-desc">With Japanese mayo</p></div>

    <div class="food-photo food-photo--fried" style="top:114px;height:159px" role="img" aria-label="Photo of fried crab claws on lettuce"></div>
    <div class="food-photo food-photo--fried" style="top:283px;height:158px" role="img" aria-label="Photo of a crumbed crab claw on lettuce"></div>

    <div class="divider" style="top:467px"></div>

    <h2 class="section-title section-title--sweets" style="top:492px">Japanese-style<br>sweets</h2>
    <div class="food-photo food-photo--dessert" style="top:495px;height:131px" role="img" aria-label="Photo of green tea ice cream in a dark bowl"></div>

    <div class="menu-item" style="top:579px"><div class="item-row"><span class="item-name">Black Sesame Ice cream</span><span class="item-leader"></span><span class="item-price">$4.5</span></div></div>
    <div class="menu-item" style="top:609px"><div class="item-row"><span class="item-name">Green tea Ice cream</span><span class="item-leader"></span><span class="item-price">$4.5</span></div></div>

    <div class="divider" style="top:651px"></div>

    <div class="menu-item" style="top:677px"><div class="item-row"><span class="item-name">Japanese Green Tea</span><span class="item-leader"></span><span class="item-each">cup</span><span class="item-price">$2</span></div></div>

    <div class="blossom-art" role="img" aria-label="Pink cherry blossom flower ornament"></div>

    <footer class="page-footer">T14 CORAL BAY SHOPPING CENTRE<span class="sep">•</span>OPEN 7 DAYS A WEEK 10AM – 9PM</footer>
  </div>
</section>

</body>
</html>
```